need corporate, modern business card created for Consulting Company

I need a slick business card using elements from my website, as well as, integrating my pixelforge-created logo (see files).

The business card needs to be:
1. Corporate and modern
2. Clean and professional

I've included a PSD with the logo/icon that you can use to create it. Feel free to try a metallic finish on the logo, make it bigger/small, underlay it. Whatever you need to do to make my card stand out.

Try a black background, or white background or gray.

The idea is for my card to be memorable as well as professional and corporate.

Target Market(s)

Corporate business in the US and Canada.

Industry/Entity Type

Business

Contact Information for Business Card

Enterprise Advancing Solutions
Martin Coble, Senior Partner
office: 1 877 555 0143
mobile: 1 519 555 0172
website: http://www.velmorant.com

Requirements
Must have
• Card-related information
• corporate, yet modern
• clean and professional
• incorporate the icon only
• must have an editable form when complete!
Nice to have
• metallic icon might be cool
• try it with white or black

```html
<!DOCTYPE html>
<html lang="en">
<head>
<meta charset="utf-8">
<title>Velmorant Business Card</title>
<link href="https://fonts.googleapis.com/css2?family=Mulish:wght@400;700&display=swap" rel="stylesheet">
<style>
  :root {
    --backdrop: #e4e2df;
    --card: #2a2a2a;
    --ink: #ffffff;
    --ink-soft: #e6e6e6;
    --accent: #3a73c4;
    --divider: #6a6a6a;
    --mark-dark: #5a5a5a;
  }
  * { margin: 0; padding: 0; box-sizing: border-box; }
  html, body {
    width: 1200px;
    height: 1000px;
    overflow: hidden;
    background: var(--backdrop);
    font-family: "Mulish", sans-serif;
  }
  .card {
    position: absolute;
    left: 265px;
    width: 665px;
    height: 397px;
    background: var(--card);
  }
  .card--front { top: 73px; }
  .card--back { top: 532px; }

  .brand {
    position: absolute;
    display: flex;
    align-items: center;
    font-weight: 700;
    letter-spacing: 0.5px;
  }
  .brand__square {
    display: block;
    background: currentColor;
    border-radius: 3px;
  }
  .card--front .brand {
    left: 34px;
    top: 168px;
    color: var(--accent);
    font-size: 40px;
    gap: 12px;
  }
  .card--front .brand__square { width: 30px; height: 30px; }
  .card--back .brand {
    left: 0;
    right: 0;
    top: 130px;
    justify-content: center;
    color: var(--mark-dark);
    font-size: 68px;
    gap: 20px;
  }
  .card--back .brand__square { width: 54px; height: 54px; }

  .divider {
    position: absolute;
    left: 325px;
    top: 99px;
    width: 1px;
    height: 200px;
    background: var(--divider);
  }
  .contact {
    position: absolute;
    left: 353px;
    top: 112px;
    color: var(--ink);
  }
  .contact__name {
    font-size: 21px;
    font-weight: 700;
    line-height: 1.1;
  }
  .contact__title {
    font-size: 17px;
    font-weight: 400;
    color: var(--ink-soft);
    margin-top: 2px;
  }
  .contact__list {
    list-style: none;
    margin-top: 20px;
  }
  .contact__item {
    display: flex;
    align-items: center;
    gap: 6px;
    font-size: 17px;
    line-height: 22px;
    color: var(--ink-soft);
  }
  .contact__icon {
    width: 14px;
    height: 14px;
    fill: var(--accent);
    flex: none;
  }
  .contact__tagline {
    margin-top: 17px;
    font-size: 17px;
    font-weight: 700;
  }
</style>
</head>
<body>
  <section class="card card--front">
    <div class="brand"><span class="brand__square"></span>velmorant</div>
    <div class="divider"></div>
    <div class="contact">
      <p class="contact__name">Martin Coble</p>
      <p class="contact__title">Senior Partner</p>
      <ul class="contact__list">
        <li class="contact__item">
          <svg class="contact__icon" viewBox="0 0 16 16" aria-hidden="true"><path d="M4 1 L6.5 1 L7.5 4.5 L5.8 5.8 C6.6 7.8 8.2 9.4 10.2 10.2 L11.5 8.5 L15 9.5 L15 12 C15 13.6 13.6 15 12 15 C6 15 1 10 1 4 C1 2.4 2.4 1 4 1 Z"/></svg>
          1 519 555 0172
        </li>
        <li class="contact__item">
          <svg class="contact__icon" viewBox="0 0 16 16" aria-hidden="true"><path d="M1 5 C1 3 4 2 8 2 C12 2 15 3 15 5 L15 6 L11 6 L11 4.5 L5 4.5 L5 6 L1 6 Z M4 7 L12 7 L14 14 L2 14 Z"/></svg>
          1 877 555 0143
        </li>
        <li class="contact__item">
          <svg class="contact__icon" viewBox="0 0 16 16" aria-hidden="true"><path fill-rule="evenodd" d="M8 1 A7 7 0 1 1 8 15 A7 7 0 1 1 8 1 Z M8 2.3 C6.8 3.6 6.2 5.6 6.1 7.4 L9.9 7.4 C9.8 5.6 9.2 3.6 8 2.3 Z M2.4 7.4 L4.9 7.4 C5 5.8 5.4 4.2 6.2 2.9 C4.1 3.5 2.6 5.3 2.4 7.4 Z M11.1 7.4 L13.6 7.4 C13.4 5.3 11.9 3.5 9.8 2.9 C10.6 4.2 11 5.8 11.1 7.4 Z M2.4 8.6 C2.6 10.7 4.1 12.5 6.2 13.1 C5.4 11.8 5 10.2 4.9 8.6 Z M6.1 8.6 C6.2 10.4 6.8 12.4 8 13.7 C9.2 12.4 9.8 10.4 9.9 8.6 Z M11.1 8.6 C11 10.2 10.6 11.8 9.8 13.1 C11.9 12.5 13.4 10.7 13.6 8.6 Z"/></svg>
          www.velmorant.com
        </li>
      </ul>
      <p class="contact__tagline">Enterprise Advancing Solutions</p>
    </div>
  </section>

  <section class="card card--back">
    <div class="brand"><span class="brand__square"></span>velmorant</div>
  </section>
</body>
</html>
```